Quillstead Realty Newsletter Template

Hello! I need a real estate brokerage newlestter template using my branding and logo. There should be categories of market updates, community news, trends in home design, listing spotlights, events around town, client story highlight. This will be emailed to my clients quarterly through constant contact. Should be a pdf form that I can edit in canvas . Should include my headshot somewhere and my contact information: Odalys Prewitt, Quillstead Realty. 87 Tamsin Quay Boston MA 02190, odalys@quillsteadharbor.com (617) 555-0193

Industry/Entity Type

real estate

Font styles to use
Serif

Requirements
Must have
• navy, white gold

```html
<!DOCTYPE html>
<html lang="en">
<head>
<meta charset="utf-8">
<title>Quillstead Realty Newsletter</title>
<link href="https://fonts.googleapis.com/css2?family=Lora:wght@400;500&family=Mulish:wght@400;600;700;800&display=swap" rel="stylesheet">
<style>
  :root {
    --navy: #27365a;
    --navy-deep: #223050;
    --gold: #e2b763;
    --gold-soft: #ead5a8;
    --grey: #efefef;
    --white: #ffffff;
    --ink: #2a2f3a;
    --rule-dark: #3f4c6e;
  }
  * { margin: 0; padding: 0; box-sizing: border-box; }
  html, body { width: 1200px; height: 5278px; overflow: hidden; background: var(--white); }
  body { position: relative; font-family: "Mulish", sans-serif; color: var(--ink); }
  .abs { position: absolute; }
  .section-title {
    position: absolute; left: 0; width: 1200px; text-align: center;
    font-family: "Mulish", sans-serif; font-weight: 800; font-size: 47px;
    letter-spacing: 7px; color: var(--navy); line-height: 1;
  }

  /* Header */
  .masthead { left: 0; top: 0; width: 1200px; height: 408px; background: var(--navy); }
  .brand-name {
    left: 0; top: 176px; width: 1200px; text-align: center;
    font-family: "Mulish", sans-serif; font-weight: 600; color: var(--white);
    font-size: 54px; line-height: 1; letter-spacing: 0.5px;
  }
  .tagline {
    left: 0; top: 480px; width: 1200px; text-align: center;
    font-family: "Lora", serif; font-size: 42px; letter-spacing: 5.5px; color: var(--ink);
  }

  /* Market updates */
  .market { left: 0; top: 588px; width: 1200px; height: 776px; background: var(--grey); }
  .photo { background: linear-gradient(160deg, #9cbfe0 0%, #8a7d70 45%, #5e7a45 100%); }
  .sold-head { left: 723px; top: 792px; font-family: "Lora", serif; font-size: 53px; color: var(--navy); line-height: 1; }
  .sold-rule { left: 723px; top: 872px; width: 404px; height: 3px; background: var(--gold); }
  .sold-addr { left: 723px; top: 922px; font-weight: 700; font-size: 32px; line-height: 39px; color: var(--ink); }
  .sold-copy { left: 723px; top: 1040px; width: 400px; font-size: 26.5px; line-height: 39px; color: var(--ink); }

  /* Listings */
  .listing-name { font-family: "Lora", serif; font-size: 44px; color: var(--navy); line-height: 1; }
  .listing-addr { font-size: 27.5px; line-height: 39px; color: var(--ink); }
  .btn {
    left: 465px; top: 2071px; width: 270px; height: 73px; background: var(--gold);
    color: var(--navy); font-weight: 800; font-size: 29px; text-align: center; line-height: 73px;
  }

  /* Trends */
  .trends { left: 0; top: 2257px; width: 1200px; height: 805px;
    background: linear-gradient(100deg, #4d5366 0%, #5a5a68 40%, #4e5568 100%); }
  .year { left: 0; top: 2380px; width: 1200px; text-align: center; font-family: "Lora", serif;
    font-size: 126px; color: var(--gold); line-height: 1; }
  .year-rule { top: 2448px; height: 3px; width: 96px; background: var(--gold); }
  .trends-head { left: 0; top: 2517px; width: 1200px; text-align: center; font-weight: 800;
    font-size: 52px; letter-spacing: 8px; color: var(--gold); line-height: 1; }
  .trends-copy { left: 100px; width: 1000px; text-align: center; color: var(--white);
    font-size: 28.5px; line-height: 39px; }

  /* News */
  .news { left: 0; top: 3062px; width: 1200px; height: 823px; background: var(--grey); }
  .news-thumb { left: 76px; width: 217px; height: 152px; }
  .news-date { left: 350px; font-size: 28px; color: var(--ink); line-height: 1; }
  .news-title { left: 350px; font-family: "Lora", serif; font-size: 33px; color: var(--navy); line-height: 1; }
  .news-more { left: 350px; font-size: 22px; color: var(--navy); line-height: 1; }
  .news-rule { left: 350px; width: 107px; height: 3px; background: var(--gold); }

  /* Testimonial */
  .testimonial-bg { left: 0; top: 3885px; width: 1200px; height: 780px; background: #fbfbfb; }
  .quote-frame { left: 76px; top: 4037px; width: 1048px; height: 430px; border: 2px solid var(--gold-soft); }
  .quote-gap { left: 487px; top: 4030px; width: 226px; height: 16px; background: #fbfbfb; }
  .quote-mark { left: 0; top: 3935px; width: 1200px; text-align: center; font-family: "Lora", serif;
    font-weight: 500; font-size: 260px; line-height: 1; color: var(--gold); }
  .quote-copy { left: 150px; top: 4125px; width: 900px; text-align: center; font-size: 28.5px; line-height: 39.5px; color: var(--ink); }
  .quote-by { left: 0; top: 4363px; width: 1200px; text-align: center; font-size: 28.5px; color: var(--ink); }

  /* Footer */
  .agent-name { left: 0; top: 4868px; width: 1200px; text-align: center; font-family: "Lora", serif;
    font-size: 54px; color: var(--white); line-height: 1; }
  .agent-firm { left: 0; top: 4930px; width: 1200px; text-align: center; font-size: 27px;
    letter-spacing: 6px; color: var(--gold); line-height: 1; }
  .contact { left: 125px; font-size: 28.5px; color: var(--white); line-height: 1; }
  .footer-name { left: 830px; top: 5064px; width: 310px; text-align: right; font-family: "Mulish", sans-serif;
    font-weight: 600; font-size: 30px; line-height: 1; color: var(--white); }
  .footer-rule { left: 76px; top: 5176px; width: 1048px; height: 2px; background: var(--rule-dark); }
  .copyright { left: 0; top: 5208px; width: 1200px; text-align: center; font-size: 22.5px; color: var(--white); }
</style>
</head>
<body>

<!-- Masthead -->
<div class="abs masthead"></div>
<div class="abs brand-name">Quillstead Realty</div>
<div class="abs tagline">CLASSIC PATTERN, ELEVATED EXPERIENCE</div>

<!-- Market updates -->
<div class="abs market"></div>
<svg class="abs" style="left:0;top:1290px" width="1200" height="80" viewBox="0 0 1200 80">
  <path d="M0,72 L0,70 C220,20 520,22 820,30 C1000,34 1120,40 1200,44 L1200,80 L0,80 Z" fill="#ffffff"/>
</svg>
<div class="section-title" style="top:671px">MARKET UPDATES</div>
<div class="abs photo" style="left:76px;top:766px;width:598px;height:459px" role="img" aria-label="Photo of a two-storey family home with a double garage"></div>
<div class="abs sold-head">SOLD IN 3 DAYS!</div>
<div class="abs sold-rule"></div>
<div class="abs sold-addr">96 Oxbow Rd. In<br>Framingham, MA</div>
<div class="abs sold-copy">Lorem ipsum dolor sit amet, consectetur adipiscing elit, sed do eiusmod tempor incididunt ut labore et dolore.</div>

<!-- Listings -->
<div class="section-title" style="top:1448px">PROPERTY LISTINGS</div>

<div class="abs" style="left:76px;top:1534px;width:334px;height:248px;background:linear-gradient(180deg,#e6e3de,#a89a86)" role="img" aria-label="Photo of a bright kitchen with island seating"></div>
<div class="abs" style="left:432px;top:1534px;width:336px;height:248px;background:linear-gradient(180deg,#9ac2e6 0%,#8b8d96 50%,#6d9a4a 100%)" role="img" aria-label="Photo of a two-storey house exterior"></div>
<div class="abs" style="left:790px;top:1534px;width:336px;height:248px;background:linear-gradient(180deg,#eeeeee,#b9b3aa)" role="img" aria-label="Photo of a modern living room"></div>

<div class="abs listing-name" style="left:76px;top:1818px">Property 1</div>
<div class="abs listing-name" style="left:432px;top:1818px">Property 2</div>
<div class="abs listing-name" style="left:790px;top:1818px">Property 3</div>

<svg class="abs" style="left:76px;top:1890px" width="32" height="44" viewBox="0 0 24 34"><path d="M12 0C5.4 0 0 5.2 0 11.7 0 20 12 34 12 34s12-14 12-22.3C24 5.2 18.6 0 12 0z" fill="#e2b763"/><circle cx="12" cy="11.5" r="4.5" fill="#fff"/></svg>
<svg class="abs" style="left:432px;top:1890px" width="32" height="44" viewBox="0 0 24 34"><path d="M12 0C5.4 0 0 5.2 0 11.7 0 20 12 34 12 34s12-14 12-22.3C24 5.2 18.6 0 12 0z" fill="#e2b763"/><circle cx="12" cy="11.5" r="4.5" fill="#fff"/></svg>
<svg class="abs" style="left:790px;top:1890px" width="32" height="44" viewBox="0 0 24 34"><path d="M12 0C5.4 0 0 5.2 0 11.7 0 20 12 34 12 34s12-14 12-22.3C24 5.2 18.6 0 12 0z" fill="#e2b763"/><circle cx="12" cy="11.5" r="4.5" fill="#fff"/></svg>

<div class="abs listing-addr" style="left:127px;top:1881px">124 Put Location<br>Here, Location<br>Framingham MA</div>
<div class="abs listing-addr" style="left:483px;top:1881px">80 Put Location<br>Here, Location<br>Framingham MA</div>
<div class="abs listing-addr" style="left:841px;top:1881px">48 Put Location<br>Here, Location<br>Framingham MA</div>

<div class="abs btn">VIEW MORE</div>

<!-- Design trends -->
<div class="abs trends" role="img" aria-label="Dimmed photo of a living room with a leather sofa and plants"></div>
<div class="abs year-rule" style="left:354px"></div>
<div class="abs year-rule" style="left:748px"></div>
<div class="abs year">2024</div>
<div class="abs trends-head">DESIGN TRENDS</div>
<div class="abs trends-copy" style="top:2592px">Enim ad minim veniam, quis nostrud exercitation ullamco laboris nisi ut aliquip ex ea commodo consequat.</div>
<div class="abs trends-copy" style="top:2709px">Duis aute irure dolor in reprehenderit in voluptate velit esse cillum dolore eu fugiat nulla pariatur. Excepteur sint occaecat cupidatat non proident, sunt in culpa qui officia deserunt mollit anim id est laborum.</div>
<div class="abs trends-copy" style="top:2866px">Lorem ipsum dolor sit amet, consectetur adipiscing elit, sed do eiusmod tempor incididunt ut labore et dolore magna aliqua.</div>

<!-- News & events -->
<div class="abs news"></div>
<div class="section-title" style="top:3172px">NEWS &amp; EVENTS</div>

<div class="abs news-thumb" style="top:3267px;background:linear-gradient(135deg,#3a3632,#7a6a55)" role="img" aria-label="Photo of a team meeting around a table"></div>
<div class="abs news-date" style="top:3276px">Oct 5, 2024</div>
<div class="abs news-title" style="top:3310px">Boston Fall Real Estate Market Trends 2024</div>
<div class="abs news-more" style="top:3364px">read more</div>
<div class="abs news-rule" style="top:3401px"></div>

<div class="abs news-thumb" style="top:3465px;background:linear-gradient(135deg,#d9d3cc,#c0683a)" role="img" aria-label="Photo of a model house beside paperwork and a calculator"></div>
<div class="abs news-date" style="top:3475px">Mar 12, 2024</div>
<div class="abs news-title" style="top:3509px">The Power of a CMA</div>
<div class="abs news-more" style="top:3563px">read more</div>
<div class="abs news-rule" style="top:3600px"></div>

<div class="abs news-thumb" style="top:3664px;background:linear-gradient(135deg,#2a2d30,#8c8f92)" role="img" aria-label="Photo of a client signing documents with an agent"></div>
<div class="abs news-date" style="top:3673px">Mar 9, 2024</div>
<div class="abs news-title" style="top:3707px">What’s going on with Interest Rates?</div>
<div class="abs news-more" style="top:3761px">read more</div>
<div class="abs news-rule" style="top:3798px"></div>

<!-- Testimonial -->
<div class="abs testimonial-bg"></div>
<div class="abs quote-frame"></div>
<div class="abs quote-gap"></div>
<div class="abs quote-mark">“</div>
<div class="abs quote-copy">Odalys is amazing! Honestly not enough words to describe the amazing help she has been for me and my husband getting our first house. Any concern or question and she’s quick to solve it. She’s become a friend to us and we’ll always go to her in the future with full confidence. Thanks Odalys!</div>
<div class="abs quote-by">-Marisol T.</div>

<!-- Footer -->
<svg class="abs" style="left:0;top:4630px" width="1200" height="648" viewBox="0 0 1200 648">
  <path d="M0,90 C250,70 520,40 760,20 C950,6 1100,14 1200,20 L1200,648 L0,648 Z" fill="#27365a"/>
</svg>
<svg class="abs" style="left:448px;top:4556px" width="304" height="304" viewBox="0 0 304 304">
  <circle cx="152" cy="152" r="150" fill="#ffffff" stroke="#e2b763" stroke-width="2.5"/>
</svg>
<div class="abs" style="left:470px;top:4578px;width:260px;height:260px;border-radius:50%;background:radial-gradient(circle at 50% 40%,#c9a38a 0%,#8a6248 55%,#d8d8d8 100%)" role="img" aria-label="Headshot of agent Odalys Prewitt"></div>
<div class="abs agent-name">Odalys Prewitt</div>
<div class="abs agent-firm">QUILLSTEAD REALTY</div>

<svg class="abs" style="left:80px;top:5019px" width="22" height="30" viewBox="0 0 24 34"><path d="M12 0C5.4 0 0 5.2 0 11.7 0 20 12 34 12 34s12-14 12-22.3C24 5.2 18.6 0 12 0z" fill="#e2b763"/><circle cx="12" cy="11.5" r="4.5" fill="#27365a"/></svg>
<svg class="abs" style="left:77px;top:5069px" width="28" height="20" viewBox="0 0 28 20"><rect width="28" height="20" rx="2" fill="#e2b763"/><path d="M1 2 L14 11 L27 2" fill="none" stroke="#27365a" stroke-width="2"/></svg>
<svg class="abs" style="left:78px;top:5110px" width="26" height="26" viewBox="0 0 24 24"><path d="M6.6 10.8c1.4 2.8 3.8 5.1 6.6 6.6l2.2-2.2c.3-.3.7-.4 1-.2 1.1.4 2.3.6 3.6.6.6 0 1 .4 1 1V20c0 .6-.4 1-1 1C10.6 21 3 13.4 3 4c0-.6.4-1 1-1h3.5c.6 0 1 .4 1 1 0 1.3.2 2.5.6 3.6.1.3 0 .7-.2 1L6.6 10.8z" fill="#e2b763"/></svg>
<div class="abs contact" style="top:5020px">87 Tamsin Quay Boston MA 02190</div>
<div class="abs contact" style="top:5065px">odalys@quillsteadharbor.com</div>
<div class="abs contact" style="top:5110px">(617) 555-0193</div>

<div class="abs footer-name">Quillstead Realty</div>
<div class="abs footer-rule"></div>
<div class="abs copyright">Copyright © 2024 Quillstead Realty &nbsp;- All Rights Reserved.</div>

</body>
</html>
```